Business Card Design

We Need a business card design for my company based in Tv Radio and music Productions and hunt Talent.

Industry/Entity Type

Business

Contact Information for Business Card

BrentaVue Production's, Teodor Vignoles,Cell Phone 318 4957310
Musician, Productor, Hunt Talent. Miami Fla. www.brentavue.net Mail. teodorvignoles@mailvana.com

```html
<!DOCTYPE html>
<html lang="en">
<head>
<meta charset="utf-8">
<title>BrentaVue Production's – Business Card</title>
<link href="https://fonts.googleapis.com/css2?family=Cabin:wght@400;500&display=swap" rel="stylesheet">
<style>
  :root {
    --stage-black: #060504;
    --curtain-dark: #15120e;
    --curtain-mid: #2a251d;
    --spot-warm: #d8cfae;
    --spot-haze: rgba(190, 175, 130, 0.35);
    --text-white: #ffffff;
    --text-glow: rgba(255, 245, 220, 0.55);
  }
  html, body {
    margin: 0;
    padding: 0;
    width: 1200px;
    height: 702px;
    overflow: hidden;
    background: var(--stage-black);
  }
  .card {
    position: relative;
    width: 1200px;
    height: 702px;
    overflow: hidden;
    font-family: "Cabin", "Gill Sans", sans-serif;
    color: var(--text-white);
  }
  .stage-backdrop {
    position: absolute;
    inset: 0;
    background:
      radial-gradient(ellipse 160px 160px at 250px 190px, var(--spot-warm) 0%, rgba(216,207,174,0.5) 40%, transparent 100%),
      radial-gradient(ellipse 520px 300px at 520px 330px, var(--spot-haze) 0%, transparent 75%),
      radial-gradient(ellipse 700px 500px at 300px 300px, var(--curtain-mid) 0%, transparent 80%),
      linear-gradient(90deg, var(--curtain-dark) 0%, var(--stage-black) 100%);
  }
  .card-text {
    position: absolute;
    left: 0;
    width: 100%;
    margin: 0;
    line-height: 1;
    text-align: center;
    white-space: nowrap;
    text-shadow: 0 0 6px var(--text-glow);
  }
  .company   { top: 111px; font-size: 29px; left: 0; width: 1200px; transform: translateX(0); }
  .name      { top: 232px; font-size: 55px; }
  .roles     { top: 309px; font-size: 40px; }
  .phone     { top: 370px; font-size: 33px; }
  .city      { top: 472px; font-size: 33px; }
  .website   { top: 514px; font-size: 38px; }
  .email     { top: 566px; font-size: 31px; }
  .phone-icon {
    width: 20px;
    height: 30px;
    vertical-align: -3px;
    margin-right: 6px;
  }
</style>
</head>
<body>
  <div class="card">
    <div class="stage-backdrop" role="img" aria-label="Photograph of a vintage stage spotlight shining warm light across a dark theatre curtain with sparkles"></div>

    <p class="card-text company">BrentaVue Production's</p>
    <p class="card-text name">Teodor Vignoles</p>
    <p class="card-text roles">Musician, Productor, Hunt Talent.</p>
    <p class="card-text phone">
      <svg class="phone-icon" viewBox="0 0 20 30" aria-hidden="true">
        <rect x="2" y="1" width="16" height="28" rx="3" fill="none" stroke="#fff" stroke-width="2"/>
        <rect x="5" y="4" width="10" height="7" fill="#fff"/>
        <g fill="#fff">
          <rect x="5" y="14" width="2.5" height="2.5"/><rect x="8.75" y="14" width="2.5" height="2.5"/><rect x="12.5" y="14" width="2.5" height="2.5"/>
          <rect x="5" y="18.5" width="2.5" height="2.5"/><rect x="8.75" y="18.5" width="2.5" height="2.5"/><rect x="12.5" y="18.5" width="2.5" height="2.5"/>
          <rect x="5" y="23" width="2.5" height="2.5"/><rect x="8.75" y="23" width="2.5" height="2.5"/><rect x="12.5" y="23" width="2.5" height="2.5"/>
        </g>
      </svg>318 4957310
    </p>
    <p class="card-text city">Miami Fla.</p>
    <p class="card-text website">www.brentavue.net</p>
    <p class="card-text email">teodorvignoles@mailvana.com</p>
  </div>
</body>
</html>
```